CalmHaven Webpage for Integrative and Holistic Psychiatric Practice

We need a webpage designed for a medical practice that focuses on integrative and holistic psychiatry. We focus on providing care to mothers and families. The name of the company is Calm Haven, incorporated, A Professional Medical Corporation.

We'd like the color palette to be earthy/natural with the same look and feel as our logo that's attached. We're not set on anything, so feel free to have fun with the palette. We just want it to be warm and inviting in particular for Moms!

We'd like to have our logo in the top left with links below it either centered or to the right. We really like websites like http://www.brightmeadowclinic.example/home.html and http://www.tarnwickmindpartners.example/site/ to give you an idea of what we're looking for.

For links, we're looking for the following. Dummy text is fine, we're still getting content together:

* Home
* About Us - this page would have headings for Directions, Staff, Appointment Scheduling
* Services Provided - headings for 8 different services
* Patient Resources - headings for Patient Forms, Fees, Articles
* FAQ
* Contact Us

The webpage will be hosted as an Office 365 Public Website, so feel free to use whatever SharePoint integration you would like, but it's not necessary.

Thank you!

```html
<!DOCTYPE html>
<html lang="en">
<head>
<meta charset="utf-8">
<title>CalmHaven – Integrative &amp; Holistic Psychiatry</title>
<link href="https://fonts.googleapis.com/css2?family=Lato:ital,wght@0,300;0,400;0,700;1,400&family=Oswald:wght@400&display=swap" rel="stylesheet">
<style>
:root{
  --brown:#5b2a04;
  --brown-dark:#4a2203;
  --green:#2f6d0b;
  --green-light:#4d9a1a;
  --text:#333;
  --muted:#555;
  --grey-bg:#f1f1f0;
  --white:#fff;
}
*{box-sizing:border-box;margin:0;padding:0}
html,body{width:853px;height:1200px;overflow:hidden}
body{position:relative;font-family:"Lato",sans-serif;color:var(--text);background:var(--white)}
.abs{position:absolute}
a{color:inherit;text-decoration:none}

/* header */
.site-header{left:0;top:0;width:853px;height:79px;background:var(--white);border-top:2px solid var(--brown)}
.brand{left:95px;top:22px;display:flex;align-items:center;gap:8px;font-size:22px;font-weight:700;color:var(--brown)}
.brand-dot{width:26px;height:26px;border-radius:50%;background:var(--green)}
.call{right:93px;top:30px;display:flex;align-items:center;gap:6px;font-size:15px;color:var(--green)}
.call b{color:#333;font-weight:400}
.call-icon{width:18px;height:18px;border-radius:50%;background:var(--green);display:flex;align-items:center;justify-content:center}

.main-nav{left:0;top:79px;width:853px;height:33px;background:var(--brown)}
.main-nav ul{list-style:none;display:flex;position:absolute;left:93px;top:0;height:33px}
.main-nav li{height:33px;display:flex;align-items:center;justify-content:center;font-size:10.5px;font-weight:700;color:var(--white);border-right:1px solid #7a4418}
.main-nav li:last-child{border-right:none}
.main-nav li.active{background:var(--green)}

/* hero */
.hero{left:0;top:112px;width:853px;height:305px;background:linear-gradient(180deg,#b9c6a0 0%,#d7b7a6 55%,#c98aa0 100%)}
.hero-curve{left:0;top:370px;width:853px;height:70px}
.slider-tab{left:381px;top:354px;width:90px;height:24px;background:var(--brown);border-radius:6px 6px 0 0;display:flex;align-items:center;justify-content:center;gap:5px}
.slider-tab span{width:10px;height:10px;border-radius:50%;background:#ddd}
.slider-tab span.on{background:var(--green);box-shadow:0 0 0 1.5px #ddd}

/* features */
.features{left:93px;top:376px;width:667px;height:190px;background:var(--white);border-top:3px solid var(--brown);display:flex;box-shadow:0 6px 10px rgba(0,0,0,.05)}
.feature{flex:1;text-align:center;position:relative}
.feature-badge{display:block;margin:0 auto}
.feature h2{font-weight:400;font-size:18px;color:#333;margin-top:8px}
.feature p{font-size:9px;line-height:14px;color:var(--muted);width:190px;margin:10px auto 0}
.btn{display:inline-block;background:var(--green);color:var(--white);font-size:10px;font-weight:700;padding:5px 7px;border-radius:2px;border:1px solid #1f4d06}
.feature .btn{margin-top:12px}

/* welcome */
.welcome{left:100px;top:588px;width:420px}
.welcome-title{display:flex;align-items:center;gap:8px;font-size:16px;color:var(--brown)}
.welcome-title .dot{width:26px;height:20px;border-radius:50%;background:var(--green)}
.welcome-title .rule{flex:1;height:1px;background:#ccc;margin-left:10px}
.welcome p{font-size:9px;line-height:14.5px;color:var(--muted);margin-top:14px}
.welcome .btn{margin-top:10px}
.video{left:560px;top:587px;width:193px;height:146px;border:1px solid #ccc;padding:3px;background:var(--white)}
.video-frame{width:185px;height:118px;background:linear-gradient(135deg,#6f8f4e,#b69a74 60%,#8f8a6e)}
.video-bar{width:185px;height:20px;background:#111;display:flex;align-items:center;gap:6px;padding:0 6px;font-size:8px;color:#fff;font-weight:700}
.video-bar .track{flex:1;height:4px;background:#555;border-radius:2px}

/* grey section */
.news-band{left:0;top:767px;width:853px;height:200px;background:var(--grey-bg)}
.section-title{font-size:20px;font-weight:400;color:#333}
.section-title em{font-style:normal;color:var(--green)}
.arrows{display:flex;gap:3px}
.arrows span{width:13px;height:13px;border-radius:50%;border:1px solid #999}
.news{left:100px;top:783px;width:305px}
.head-row{display:flex;justify-content:space-between;align-items:center;padding-bottom:5px;border-bottom:1px solid #ccc}
.news-item{display:flex;gap:12px;padding:12px 0 14px;border-bottom:1px solid #ddd}
.news-item:last-child{border-bottom:none}
.date{width:35px;flex:none;text-align:center;font-family:"Oswald",sans-serif;color:#fff}
.date .d{background:var(--green);font-size:17px;height:24px;line-height:24px}
.date .m{background:var(--brown);font-size:9px;height:13px;line-height:13px}
.news-item h3{font-size:9.5px;font-weight:700;color:#333}
.news-item p{font-size:9px;line-height:15px;color:var(--muted)}
.divider{left:424px;top:783px;width:1px;height:150px;background:#ddd}
.testimonials{left:449px;top:783px;width:303px}
.avatar{left:447px;top:822px;width:76px;height:76px;border-radius:50%;border:3px solid #fff;box-shadow:0 0 0 1px #ccc;background:linear-gradient(160deg,#c9a37b,#8a5a3a)}
.quote{left:545px;top:824px;width:210px;font-size:9.5px;font-style:italic;line-height:17.5px;color:#444}
.quote-by{left:545px;top:904px;font-size:11px;font-weight:700;color:var(--brown)}

/* footer */
.footer-curve{left:0;top:925px;width:853px;height:80px}
.footer{left:0;top:995px;width:853px;height:205px;background:var(--brown);color:#fff}
.fcol{top:21px}
.fcol h4{font-size:12px;font-weight:700;padding-bottom:8px;border-bottom:1px solid #7a4418;margin-bottom:8px}
.fcol ul{list-style:none;font-size:9.5px;line-height:18.6px}
.fcol p{font-size:8.5px;line-height:12px}
.email-field{margin-top:10px;width:147px;height:18px;background:#fff;border-radius:2px;font-size:8px;font-style:italic;color:#555;padding:4px 10px}
.footer .btn{margin-top:12px;width:81px;text-align:center;font-size:10px;border-color:#9bc07a}
.contact-row{display:flex;gap:10px;font-size:9px;line-height:13px;margin-bottom:16px;align-items:flex-start}
.contact-row svg{flex:none;margin-top:2px}
.map{left:600px;top:54px;width:160px;height:86px;border:2px solid #fff;background:linear-gradient(135deg,#e9e3c8,#b8d0e6 60%,#e5dcc0)}
.vsep{top:48px;width:1px;height:100px;background:#7a4418}
.copyright-rule{left:93px;top:162px;width:667px;height:1px;background:#7a4418}
.copyright{left:95px;top:178px;font-size:9px}
.social{left:696px;top:175px;display:flex;gap:7px}
.social span{width:16px;height:16px;background:#fff;border-radius:2px}
</style>
</head>
<body>

<header class="site-header abs">
  <a class="brand abs" href="#"><span class="brand-dot"></span>CalmHaven</a>
  <div class="call abs">
    <span class="call-icon"><svg width="10" height="10" viewBox="0 0 24 24"><path fill="#fff" d="M6.6 10.8a15.1 15.1 0 006.6 6.6l2.2-2.2c.3-.3.7-.4 1-.2 1.1.4 2.3.6 3.6.6.6 0 1 .4 1 1V20c0 .6-.4 1-1 1A17 17 0 013 4c0-.6.4-1 1-1h3.5c.6 0 1 .4 1 1 0 1.3.2 2.5.6 3.6.1.3 0 .7-.2 1z"/></svg></span>
    Call Now! <b>(555) 284-7310</b>
  </div>
</header>

<nav class="main-nav abs">
  <ul>
    <li class="active" style="width:94px">HOME</li>
    <li style="width:116px">ABOUT US</li>
    <li style="width:112px">SERVICES</li>
    <li style="width:86px">FAQ</li>
    <li style="width:165px">PATIENT RESOURCES</li>
    <li style="width:126px">CONTACT US</li>
  </ul>
</nav>

<div class="hero abs" role="img" aria-label="Photo of a smiling multi-generation family outdoors among trees"></div>
<svg class="hero-curve abs" viewBox="0 0 853 70" preserveAspectRatio="none" aria-hidden="true">
  <path d="M0 30 Q60 50 93 50 L93 70 L0 70Z" fill="#fbf0ea"/>
  <path d="M0 30 Q60 50 93 52" stroke="#5b2a04" stroke-width="3" fill="none"/>
  <path d="M853 28 Q800 46 760 52 L760 70 L853 70Z" fill="#fbf0ea"/>
  <path d="M853 28 Q800 46 760 53" stroke="#5b2a04" stroke-width="3" fill="none"/>
</svg>
<div class="slider-tab abs"><span class="on"></span><span></span><span></span><span></span></div>

<section class="features abs">
  <article class="feature">
    <svg class="feature-badge" width="56" height="60" viewBox="0 0 56 60"><path d="M0 0H56V50L28 60 0 50Z" fill="#2f6d0b"/><path d="M0 50L28 60 56 50" stroke="#5b2a04" stroke-width="2" fill="none"/><circle cx="24" cy="28" r="8" fill="none" stroke="#fff" stroke-width="4" stroke-dasharray="3 2"/><circle cx="36" cy="20" r="5" fill="none" stroke="#fff" stroke-width="3" stroke-dasharray="2 2"/></svg>
    <h2>We Services Provided</h2>
    <p>It is a long established fact that a rea distracted by the readable content of a page when looking at its layout.</p>
    <a class="btn" href="#">Read More</a>
  </article>
  <article class="feature">
    <svg class="feature-badge" width="56" height="60" viewBox="0 0 56 60"><path d="M0 0H56V50L28 60 0 50Z" fill="#2f6d0b"/><path d="M0 50L28 60 56 50" stroke="#5b2a04" stroke-width="2" fill="none"/><rect x="14" y="12" width="28" height="26" rx="2" fill="#fff"/><rect x="14" y="12" width="28" height="6" fill="#ddd"/><g fill="#2f6d0b"><rect x="18" y="22" width="4" height="4"/><rect x="26" y="22" width="4" height="4"/><rect x="34" y="22" width="4" height="4"/><rect x="18" y="30" width="4" height="4"/><rect x="26" y="30" width="4" height="4"/><rect x="34" y="30" width="4" height="4"/></g></svg>
    <h2>Appointment Scheduling</h2>
    <p>It is a long established fact that a rea distracted by the readable content of a page when looking at its layout.</p>
    <a class="btn" href="#">Read More</a>
  </article>
  <article class="feature">
    <svg class="feature-badge" width="56" height="60" viewBox="0 0 56 60"><path d="M0 0H56V50L28 60 0 50Z" fill="#2f6d0b"/><path d="M0 50L28 60 56 50" stroke="#5b2a04" stroke-width="2" fill="none"/><g fill="#fff"><circle cx="28" cy="18" r="5"/><path d="M19 36c0-7 4-11 9-11s9 4 9 11z"/><circle cx="17" cy="21" r="3.5"/><path d="M10 35c0-5 3-8 7-8l2 1-2 7z"/><circle cx="39" cy="21" r="3.5"/><path d="M46 35c0-5-3-8-7-8l-2 1 2 7z"/></g></svg>
    <h2>Patient Resources</h2>
    <p>It is a long established fact that a rea distracted by the readable content of a page when looking at its layout.</p>
    <a class="btn" href="#">Read More</a>
  </article>
</section>

<section class="welcome abs">
  <h2 class="welcome-title"><span class="dot"></span>Welcome CalmHaven<span class="rule"></span></h2>
  <p>Lorem ipsum dolor sit amet, consectetuer adipiscing elit, sed diam nonummy nibh euismod tincidunt ut laoreet dolore magna aliquam erat volutpat. Ut wisi enim ad minim veniam, quis nostrud exerci tation ullamcorper suscipit lobortis nisl ut aliquip ex ea commodo consequat. Duis autem vel eum iriure dolor in hendrerit in vulputate velit esse molestie consequat, vel illum dolore eu feugiat nulla facilisis at vero eros et accumsan et iusto odio dignissim qui blandit praesent luptatum zzril delenit augue duis dolore te feugait nulla facilisi.</p>
  <a class="btn" href="#">Read More</a>
</section>
<div class="video abs">
  <div class="video-frame" role="img" aria-label="Video still of a smiling couple outdoors"></div>
  <div class="video-bar">
    <svg width="8" height="9" viewBox="0 0 8 9"><path d="M0 0L8 4.5 0 9Z" fill="#fff"/></svg>
    <span>04:59</span><span class="track"></span><span>10:35</span>
    <svg width="9" height="9" viewBox="0 0 9 9"><path d="M0 3H2L5 0V9L2 6H0Z" fill="#fff"/></svg>
  </div>
</div>

<div class="news-band abs"></div>
<section class="news abs">
  <div class="head-row"><h2 class="section-title">Latest <em>News</em></h2><div class="arrows"><span></span><span></span></div></div>
  <div class="news-item">
    <div class="date"><div class="d">04</div><div class="m">OCT</div></div>
    <div><h3>Sed ut perspiciatis unde omnis iste natus error sit</h3><p>voluptatem accusant &nbsp;doloremque laudantium, totamrem okl aperiam, eaque ipsa quae ab illoi</p></div>
  </div>
  <div class="news-item">
    <div class="date"><div class="d">06</div><div class="m">OCT</div></div>
    <div><h3>Sed ut perspiciatis unde omnis iste natus error sit</h3><p>voluptatem accusant &nbsp;doloremque laudantium, totamrem okl aperiam, eaque ipsa quae ab illoi</p></div>
  </div>
</section>
<div class="divider abs"></div>
<section class="testimonials abs">
  <div class="head-row"><h2 class="section-title">Client <em>Testimonials</em></h2><div class="arrows"><span></span><span></span></div></div>
</section>
<div class="avatar abs" role="img" aria-label="Portrait photo of the client"></div>
<blockquote class="quote abs">Lorem ipsum sit amet co adipiscig elitsedudi eiusmod tepor incidiunt ut la dolore maa aliquan ki enim nim veni exercitation ullamco ipsum sdit amet co adipiscig elitsed do eiusmod tepor</blockquote>
<div class="quote-by abs">- Marla Quenby</div>

<svg class="footer-curve abs" viewBox="0 0 853 80" preserveAspectRatio="none" aria-hidden="true">
  <path d="M0 5 Q200 70 450 40 T853 30 V80 H0Z" fill="#3c8a0e"/>
  <path d="M0 18 Q200 78 450 50 T853 40 V80 H0Z" fill="#fff"/>
  <path d="M0 24 Q200 84 450 56 T853 46 V80 H0Z" fill="#5b2a04"/>
</svg>

<footer class="footer abs">
  <div class="fcol abs" style="left:95px;width:97px">
    <h4>Quick Links</h4>
    <ul><li>HOME</li><li>ABOUT US</li><li>SERVICES</li><li>FAQ</li><li>PATIENT RESOURCES</li><li>CONTACT US</li></ul>
  </div>
  <div class="vsep abs" style="left:207px"></div>
  <div class="fcol abs" style="left:224px;width:150px">
    <h4>Subscribe to Newsletter</h4>
    <p>Get Latest Updates By Entering Your Email Address</p>
    <div class="email-field">Email Address</div>
    <a class="btn" href="#">Subscribe</a>
  </div>
  <div class="vsep abs" style="left:391px"></div>
  <div class="fcol abs" style="left:411px;width:155px">
    <h4>Contact Us</h4>
    <div class="contact-row"><svg width="9" height="12" viewBox="0 0 9 12"><path d="M4.5 0A4.5 4.5 0 000 4.5C0 8 4.5 12 4.5 12S9 8 9 4.5A4.5 4.5 0 004.5 0Zm0 6.3a1.8 1.8 0 110-3.6 1.8 1.8 0 010 3.6Z" fill="#fff"/></svg><span>Lorem ipsum dolor sit consecte<br>No 5, zip Code: 897410</span></div>
    <div class="contact-row" style="font-weight:700;font-size:10px"><svg width="11" height="11" viewBox="0 0 24 24"><path fill="#fff" d="M6.6 10.8a15.1 15.1 0 006.6 6.6l2.2-2.2c.3-.3.7-.4 1-.2 1.1.4 2.3.6 3.6.6.6 0 1 .4 1 1V20c0 .6-.4 1-1 1A17 17 0 013 4c0-.6.4-1 1-1h3.5c.6 0 1 .4 1 1 0 1.3.2 2.5.6 3.6.1.3 0 .7-.2 1z"/></svg><span>(555) 902-1146</span></div>
    <div class="contact-row"><svg width="12" height="9" viewBox="0 0 12 9"><rect width="12" height="9" fill="#fff"/><path d="M0 0L6 5 12 0" stroke="#5b2a04" fill="none"/></svg><span>info@calmhaven.example</span></div>
  </div>
  <div class="vsep abs" style="left:580px"></div>
  <div class="fcol abs" style="left:597px;width:163px">
    <h4>Location Map</h4>
  </div>
  <div class="map abs" role="img" aria-label="Street map showing the practice location"></div>
  <div class="copyright-rule abs"></div>
  <p class="copyright abs">© 2014 CalmHaven. All Rights Reserved.</p>
  <div class="social abs" aria-label="Social links"><span></span><span></span><span></span></div>
</footer>

</body>
</html>
```